Games for Classrooms Website Redesign

The purpose of the website redesign is to freshen up the content and update it to give a more modern look and feel. It will show what we do concisely and satisfy all potential visitors. We work with primary schools and the brand is fun.About: Games for Classrooms is a scheme that brings top Zentara athletes into primary schools to inspire children to do more physical activity. We typically run a half day event at the school where the athlete does a fun fitness circuit with the children and then an inspirational assembly with a demonstration and Q&A. The children are asked to collect sponsorship money to take part in the event and a large proportion of the money raised goes back to the school in the form of a voucher for them to spend on new sports equipment. 1. To generate more leads from potential customers/schools2. To engage the children and parents more in the event and get them excited for their upcoming visit whilst setting up a fundraiser page.3. To simplify and modernise what is already there.

I have attached some ideas for each of the pages (uploaded in brief)

Here is a link to our current website: www.gamesforclassrooms.example

I have also attached a link to the sponsorship form which shows the kind of look and feel we're after.

Target Market(s)

Primary school teachers
Primary school parents

Number of Pages Required

5+ page

Requirements
Must have
• Fun, modern.
• Be built on plover scaffold

```html
<!DOCTYPE html>
<html lang="en">
<head>
<meta charset="utf-8">
<title>Games for Classrooms</title>
<link rel="stylesheet" href="https://fonts.googleapis.com/css2?family=Lato:wght@400;700;900&family=Open+Sans:wght@700&display=swap">
<style>
  :root {
    --brand-red: #c8202f;
    --brand-blue: #1f8fd6;
    --brand-green: #4caf2a;
    --ink: #1d1d1d;
    --muted: #555555;
    --school-blue: #2196e0;
    --parent-red: #df3344;
    --band-top: #ffffff;
    --band-bottom: #ececec;
    --white: #ffffff;
  }
  * { box-sizing: border-box; margin: 0; padding: 0; }
  html, body {
    width: 1200px; height: 1190px; overflow: hidden;
    background: var(--white);
    font-family: "Lato", Arial, sans-serif;
  }
  .page { position: relative; width: 1200px; height: 1190px; }

  .site-header {
    position: absolute; top: 0; left: 0; width: 1200px; height: 107px;
    background: var(--white);
  }
  .brand {
    position: absolute; left: 162px; top: 38px;
    display: flex; align-items: center; gap: 12px;
  }
  .brand-dot {
    width: 30px; height: 30px; border-radius: 50%;
    background: var(--brand-red);
  }
  .brand-name {
    font-family: "Lato", Arial, sans-serif; font-weight: 900;
    font-size: 24px; color: var(--ink); letter-spacing: -0.3px;
  }
  .menu-toggle { position: absolute; left: 978px; top: 50px; }

  .hero {
    position: absolute; top: 107px; left: 0; width: 1200px; height: 531px;
    background: linear-gradient(160deg, #a8794a 0%, #c79a6a 35%, #d8b08a 55%, #8f6a4a 100%);
  }
  .hero-title {
    position: absolute; top: 172px; left: 0; width: 1200px; text-align: center;
    font-family: "Lato", Arial, sans-serif; font-weight: 900; font-size: 45px;
    color: var(--white); letter-spacing: -0.5px;
    text-shadow: 0 1px 4px rgba(0,0,0,0.35);
  }
  .hero-text {
    position: absolute; top: 226px; left: 0; width: 1200px; text-align: center;
    font-family: "Open Sans", Arial, sans-serif; font-weight: 700; font-size: 26px;
    line-height: 35px; color: var(--white);
    text-shadow: 0 1px 4px rgba(0,0,0,0.35);
  }

  .lower {
    position: absolute; top: 638px; left: 0; width: 1200px; height: 467px;
    background: linear-gradient(180deg, var(--band-top) 0%, var(--band-top) 30%, var(--band-bottom) 100%);
  }
  .audience-card {
    position: absolute; top: 32px; width: 439px; height: 187px;
    display: flex; align-items: center; justify-content: center; gap: 18px;
    color: var(--white); text-decoration: none;
    font-family: "Lato", Arial, sans-serif; font-weight: 900; font-size: 37px;
    letter-spacing: -0.5px;
  }
  .audience-card.school { left: 161px; background: linear-gradient(135deg, #2c9fe6, #1b86cf); }
  .audience-card.parent { left: 631px; background: linear-gradient(135deg, #e6414f, #d42c3d); }

  .stats-label {
    position: absolute; left: 181px; top: 330px;
    font-weight: 700; font-size: 31px; color: var(--brand-blue);
  }
  .stat {
    position: absolute; top: 264px; width: 166px; height: 166px; border-radius: 50%;
    background: var(--white); box-shadow: 0 0 3px rgba(0,0,0,0.12);
    display: flex; flex-direction: column; align-items: center; justify-content: center;
  }
  .stat-name { font-weight: 700; font-size: 21px; color: var(--brand-green); }
  .stat-value { font-weight: 900; font-size: 36px; color: var(--brand-red); line-height: 1.2; }

  .site-footer {
    position: absolute; top: 1105px; left: 0; width: 1200px; height: 85px;
    background: var(--white); text-align: center;
    font-size: 17px; color: var(--muted); padding-top: 26px;
  }
</style>
</head>
<body>
<div class="page">
  <header class="site-header">
    <div class="brand">
      <span class="brand-dot"></span>
      <span class="brand-name">Games for Classrooms</span>
    </div>
    <svg class="menu-toggle" width="42" height="22" viewBox="0 0 42 22" aria-label="Menu">
      <rect x="0" y="0" width="42" height="3.5" rx="1.75" fill="#777"/>
      <rect x="0" y="8" width="42" height="3.5" rx="1.75" fill="#777"/>
      <rect x="0" y="16" width="42" height="3.5" rx="1.75" fill="#777"/>
    </svg>
  </header>

  <section class="hero" role="img" aria-label="Photo of two smiling children hugging on a classroom floor">
    <h1 class="hero-title">OUR MISSION</h1>
    <p class="hero-text">Our mission is to put physical health in children on a par<br>with mental health and academic excellence.</p>
  </section>

  <section class="lower">
    <a class="audience-card school" role="img" aria-label="Classroom photo with blue overlay: I'm a school">
      <svg width="72" height="72" viewBox="0 0 72 72" fill="none" stroke="#fff" stroke-width="2.5">
        <path d="M14 66V28h44v38M8 66h56M36 28V10h10v6h-10"/>
        <rect x="22" y="36" width="7" height="8"/><rect x="43" y="36" width="7" height="8"/>
        <rect x="22" y="50" width="7" height="8"/><rect x="43" y="50" width="7" height="8"/>
        <path d="M32 66V52h8v14"/>
      </svg>
      <span>I’M A SCHOOL</span>
    </a>
    <a class="audience-card parent" role="img" aria-label="Photo of parents reading with a child, red overlay: I'm a parent">
      <span>I’M A PARENT</span>
    </a>

    <h2 class="stats-label">STATS</h2>
    <div class="stat" style="left:327px"><span class="stat-name">EVENTS</span><span class="stat-value">2550</span></div>
    <div class="stat" style="left:513px"><span class="stat-name">MAURISVEL</span><span class="stat-value">1150</span></div>
    <div class="stat" style="left:693px"><span class="stat-name">ETIAM EU</span><span class="stat-value">2550</span></div>
    <div class="stat" style="left:883px"><span class="stat-name">AENEANPO</span><span class="stat-value">1150</span></div>
  </section>

  <footer class="site-footer">© 2019 Company Name &nbsp;All right reserved</footer>
</div>
</body>
</html>
```